A5 flyer required for 3D printing company

We are a 3D printing company providing our customers with customised 3D printed figurines services. And we need a double sided flyer design for our company, either to display in the shop or hand out on streets. Our website (www.tivolafigs.com.au) describes what we do and what the products look like.
The final flyer should tell our potential customers the following points:
1. We can make 3D printed figurines in incredible likeness for our customers;
2. Advanced 3D scanning and 3D printing technology;
3. Includes our price table, and grand opening 15% off for all products till 31st May 2016;
full body size Retail
8cm $159
10cm $239
12cm $279
15cm $339
18cm $449
20cm $599
Bust size
8cm $239
10cm $279
12cm $339
4. Use one or more photos supplied to show the final products compared with real person, you can use lasso tools to crop the background if you like;
5. Our contact details;
Address: Suite 7 Level 3, 516 Harlow Street Sydney, in the Brennick Building
Telephone: 02 9487 5326
Email: info@tivolafigs.com.au
Web: www.tivolafigs.com.au
The flyer should catch customers' eyes at the first sight because we will be handing out the flyers on streets as well. You can use any material used on our website (www.tivolafigs.com.au).
We would like to see the design in line with our colour scheme used for our logo. The two colours used in the logo are C70 M0 Y0 K0 and C83 M53 Y6 K0 for your reference. And the font we used in our logo is hobo std for your reference.
If you have any questions about our products or the flyer, please feel free to drop us a message.

```html
<!DOCTYPE html>
<html lang="en">
<head>
<meta charset="utf-8">
<title>Tivola Figs – 3D Printed Figurines Flyer</title>
<link href="https://fonts.googleapis.com/css2?family=Arimo:wght@700&family=Roboto+Condensed:wght@500;700&display=swap" rel="stylesheet">
<style>
  :root {
    --sky-top: #52d6f4;
    --sky-bottom: #2f8fe2;
    --headline-yellow: #ffe11a;
    --promo-red: #ea1f22;
    --white: #ffffff;
    --panel-dark: #1e1f21;
    --price-cyan: #3fd3f0;
    --footer-grey: #e7e9eb;
    --ink: #1a1a1a;
    --brand-blue: #2a86d6;
    --brand-cyan: #3cc8ee;
  }
  * { box-sizing: border-box; margin: 0; padding: 0; }
  html, body { width: 846px; height: 1200px; overflow: hidden; background: var(--white); }
  .flyer {
    position: relative;
    width: 846px;
    height: 1200px;
    overflow: hidden;
    background: linear-gradient(180deg, var(--sky-top) 0%, #45bdf0 45%, var(--sky-bottom) 100%);
    font-family: "Arimo", Arial, sans-serif;
  }
  .headline {
    position: absolute;
    color: var(--headline-yellow);
    font-weight: 700;
    font-size: 35px;
    line-height: 44px;
    letter-spacing: 0.3px;
  }
  .headline--top { left: 44px; top: 18px; }
  .headline--likeness { right: 26px; top: 586px; text-align: right; }

  .photo-frame {
    position: absolute;
    background: var(--white);
    padding: 9px;
    box-shadow: 0 2px 6px rgba(0,0,0,0.18);
  }
  .photo-frame .photo { width: 100%; height: 100%; }
  .photo-frame--wedding { left: 32px; top: 130px; width: 396px; height: 378px; transform: rotate(-1deg); }
  .photo-frame--family { left: 468px; top: 126px; width: 392px; height: 382px; transform: rotate(-2deg); }
  .photo-frame--outdoor { left: 30px; top: 568px; width: 410px; height: 404px; transform: rotate(-2deg); }
  .photo--wedding { background: linear-gradient(170deg, #f3eee8 0%, #e6ddd3 60%, #d8cdc1 100%); }
  .photo--family { background: linear-gradient(170deg, #e3e8ea 0%, #c9cfd2 60%, #aeb3b6 100%); }
  .photo--outdoor { background: linear-gradient(180deg, #6fa3e6 0%, #93adbc 40%, #89a08d 65%, #a89d86 100%); }

  .promo-band {
    position: absolute;
    left: 0; top: 505px;
    width: 846px; height: 56px;
    background: var(--promo-red);
    color: var(--white);
    font-family: "Roboto Condensed", "Arial Narrow", sans-serif;
    font-weight: 700;
    font-size: 31px;
    line-height: 56px;
    text-align: center;
    letter-spacing: 0.3px;
  }

  .price-panel {
    position: absolute;
    left: 486px; top: 710px;
    width: 340px; height: 308px;
    background: var(--panel-dark);
    font-family: "Roboto Condensed", "Arial Narrow", sans-serif;
    font-weight: 500;
    color: var(--white);
  }
  .price-column { position: absolute; top: 22px; }
  .price-column--full { left: 18px; }
  .price-column--bust { left: 186px; }
  .price-column__title {
    color: var(--price-cyan);
    font-weight: 700;
    font-size: 27px;
    line-height: 36px;
    margin-bottom: 2px;
    letter-spacing: 0.3px;
  }
  .price-title-pad { padding-left: 8px; }
  .price-row {
    display: flex;
    justify-content: flex-end;
    gap: 14px;
    font-size: 26px;
    line-height: 38px;
    width: 135px;
  }

  .footer {
    position: absolute;
    left: 0; top: 1018px;
    width: 846px; height: 182px;
    background: var(--footer-grey);
  }
  .brand-name {
    position: absolute;
    left: 48px; top: 58px;
    font-family: "Arimo", Arial, sans-serif;
    font-weight: 700;
    font-size: 46px;
    line-height: 56px;
    color: var(--brand-cyan);
  }
  .contact-list { position: absolute; left: 356px; top: 14px; list-style: none; }
  .contact-item {
    display: flex;
    align-items: flex-start;
    gap: 12px;
    font-weight: 700;
    font-size: 18.5px;
    line-height: 24px;
    color: var(--ink);
    margin-bottom: 8px;
  }
  .contact-item svg { flex: none; width: 32px; height: 26px; }
</style>
</head>
<body>
<main class="flyer">
  <h1 class="headline headline--top">Advanced 3D scanning<br>&amp; 3D printing technology</h1>

  <figure class="photo-frame photo-frame--wedding">
    <div class="photo photo--wedding" role="img" aria-label="Photo of bride and groom 3D printed figurines standing in front of a wedding cake"></div>
  </figure>
  <figure class="photo-frame photo-frame--family">
    <div class="photo photo--family" role="img" aria-label="Photo of 3D printed figurines of grandparents with a little girl on a deck"></div>
  </figure>

  <div class="promo-band">GRAND OPENING SPECIAL 15% OFF ALL PRODUCTS TIL 31 MAY</div>

  <figure class="photo-frame photo-frame--outdoor">
    <div class="photo photo--outdoor" role="img" aria-label="Photo of a young man beside his 3D printed figurine with a lake and mountains behind"></div>
  </figure>

  <h2 class="headline headline--likeness">3D printed figurines<br>in incredible likeness</h2>

  <section class="price-panel" aria-label="Price list">
    <div class="price-column price-column--full">
      <div class="price-column__title price-title-pad">FULL BODY</div>
      <div class="price-row"><span>8cm</span><span>$159</span></div>
      <div class="price-row"><span>10cm</span><span>$239</span></div>
      <div class="price-row"><span>12cm</span><span>$279</span></div>
      <div class="price-row"><span>15cm</span><span>$339</span></div>
      <div class="price-row"><span>18cm</span><span>$449</span></div>
      <div class="price-row"><span>20cm</span><span>$599</span></div>
    </div>
    <div class="price-column price-column--bust">
      <div class="price-column__title">BUST SIZED</div>
      <div class="price-row"><span>8cm</span><span>$239</span></div>
      <div class="price-row"><span>10cm</span><span>$279</span></div>
      <div class="price-row"><span>12cm</span><span>$339</span></div>
    </div>
  </section>

  <footer class="footer">
    <div class="brand-name">Tivola Figs</div>
    <ul class="contact-list">
      <li class="contact-item">
        <svg viewBox="0 0 32 26" aria-hidden="true"><path d="M16 2 L30 14 H26 V25 H19 V17 H13 V25 H6 V14 H2 Z" fill="var(--brand-blue)"/></svg>
        <span>Suite 7 Level 3, 516 Harlow Street Sydney<br>(in the Brennick Building)</span>
      </li>
      <li class="contact-item">
        <svg viewBox="0 0 32 26" aria-hidden="true"><rect x="10" y="1" width="12" height="24" rx="2" fill="none" stroke="var(--brand-blue)" stroke-width="2"/><circle cx="16" cy="21" r="1.4" fill="var(--brand-blue)"/></svg>
        <span>02 9487 5326</span>
      </li>
      <li class="contact-item">
        <svg viewBox="0 0 32 26" aria-hidden="true"><rect x="3" y="5" width="26" height="17" fill="var(--brand-blue)"/><path d="M3 5 L16 15 L29 5" fill="none" stroke="var(--white)" stroke-width="2"/></svg>
        <span>info@tivolafigs.com.au</span>
      </li>
      <li class="contact-item">
        <svg viewBox="0 0 32 26" aria-hidden="true"><rect x="5" y="3" width="22" height="15" fill="none" stroke="var(--brand-blue)" stroke-width="2"/><rect x="1" y="20" width="30" height="3" fill="var(--brand-blue)"/></svg>
        <span>www.tivolafigs.com.au</span>
      </li>
    </ul>
  </footer>
</main>
</body>
</html>
```